Brake Test Training for Coal Mining

We offer Brake Test Training for Coal Mine workers. It's a legislative requirement that workers who are tasked with performing brake testing have certain competencies to do so. We test Light Vehicles and trailers, Heavy Vehicles and Mobile Mining Equipment like Graders, Scrapers and Dump Trucks.

```html
<!DOCTYPE html>
<html lang="en">
<head>
<meta charset="utf-8">
<title>Brake Test Training for Coal Mining</title>
<link href="https://fonts.googleapis.com/css2?family=Montserrat:wght@500;700;800&display=swap" rel="stylesheet">
<style>
  :root {
    --navy: #1f2e6e;
    --navy-mid: #24407f;
    --teal: #3f95bd;
    --gold: #f2bd36;
    --white: #ffffff;
    --stage: #d9d9d9;
    --ochre-light: #d9ad4a;
    --ochre-dark: #6b5426;
  }
  * { margin: 0; padding: 0; box-sizing: border-box; }
  html, body {
    width: 1200px;
    height: 1200px;
    overflow: hidden;
    background: var(--stage);
    font-family: "Montserrat", Arial, sans-serif;
  }
  .banner {
    position: absolute;
    left: 30px;
    top: 315px;
    width: 1140px;
    height: 570px;
    overflow: hidden;
  }
  .banner-art {
    position: absolute;
    inset: 0;
    width: 1140px;
    height: 570px;
  }
  .brand {
    position: absolute;
    left: 50px;
    top: 52px;
    width: 450px;
    height: 110px;
  }
  .brand-dot {
    position: absolute;
    left: 0;
    top: 6px;
    width: 86px;
    height: 86px;
    border-radius: 50%;
    background: var(--white);
  }
  .brand-rule {
    position: absolute;
    left: 124px;
    width: 316px;
    height: 3px;
    background: var(--white);
  }
  .brand-rule.top { top: 20px; }
  .brand-rule.bottom { top: 105px; }
  .brand-name {
    position: absolute;
    left: 124px;
    top: 32px;
    width: 316px;
    text-align: center;
    color: var(--white);
    font-weight: 700;
    line-height: 1.05;
  }
  .brand-name .word { display: block; font-size: 34px; letter-spacing: 1px; }
  .brand-name .sub { display: block; font-size: 18px; letter-spacing: 0.5px; margin-top: 6px; }
  .headline {
    position: absolute;
    left: 34px;
    top: 206px;
    color: var(--white);
    line-height: 1;
  }
  .headline-main {
    display: block;
    font-size: 128px;
    font-weight: 800;
    letter-spacing: -3px;
  }
  .headline-sub {
    display: block;
    font-size: 57px;
    font-weight: 800;
    letter-spacing: -1px;
    margin-top: 6px;
    margin-left: 4px;
  }
  .headline-note {
    display: block;
    font-size: 38px;
    font-weight: 700;
    margin-top: 16px;
    margin-left: 4px;
  }
  .contact {
    position: absolute;
    left: 40px;
    top: 478px;
    display: flex;
    align-items: center;
    gap: 20px;
    color: var(--gold);
    font-size: 52px;
    font-weight: 700;
    letter-spacing: -1px;
  }
  .contact-icon { width: 52px; height: 52px; }
</style>
</head>
<body>
  <main class="banner">
    <svg class="banner-art" viewBox="0 0 1140 570" xmlns="http://www.w3.org/2000/svg">
      <defs>
        <linearGradient id="bg-blue" x1="0" y1="0" x2="1" y2="0.35">
          <stop offset="0" stop-color="var(--navy)"/>
          <stop offset="0.35" stop-color="var(--navy-mid)"/>
          <stop offset="0.62" stop-color="var(--teal)"/>
          <stop offset="1" stop-color="var(--teal)"/>
        </linearGradient>
        <linearGradient id="truck-tone" x1="0" y1="0" x2="1" y2="1">
          <stop offset="0" stop-color="var(--ochre-light)"/>
          <stop offset="1" stop-color="var(--ochre-dark)"/>
        </linearGradient>
      </defs>
      <rect class="bg" width="1140" height="570" fill="url(#bg-blue)"/>
      <path class="accent-gold" d="M675 0 C700 250 610 450 460 570 L1140 570 L1140 0 Z" fill="var(--gold)"/>
      <path class="accent-white" d="M891 0 C780 80 690 300 675 570 L1140 570 L1140 0 Z" fill="var(--white)"/>
      <rect class="truck-photo" x="540" y="60" width="600" height="460" rx="18"
            fill="url(#truck-tone)" role="img"
            aria-label="Photo of a large yellow mining haul truck loaded with coal, seen from the front left"/>
    </svg>

    <div class="brand">
      <span class="brand-dot"></span>
      <span class="brand-rule top"></span>
      <p class="brand-name"><span class="word">RIDGELINE</span><span class="sub">OPERATOR TRAINING</span></p>
      <span class="brand-rule bottom"></span>
    </div>

    <h1 class="headline">
      <span class="headline-main">BRAKE</span>
      <span class="headline-sub">TEST TRAINING</span>
      <span class="headline-note">FOR COAL MINING</span>
    </h1>

    <p class="contact">
      <svg class="contact-icon" viewBox="0 0 52 52" aria-hidden="true">
        <circle cx="26" cy="26" r="26" fill="var(--gold)"/>
        <path d="M18 13 C15 14 13 17 14 21 C16 29 23 36 31 38 C35 39 38 37 39 34 L34 29 L30 31 C26 29 23 26 21 22 L23 18 Z" fill="var(--navy)"/>
      </svg>
      <span class="contact-number">1300 628 940</span>
    </p>
  </main>
</body>
</html>
```